K & R Acreage Works. Business card design

We need a business card designed for a new business. We have a bulldozer and tractor service. We clear land and make wildlife food plots. We provide disking, bush hogging, and site prep services.
I have attached an image of a business card that I like and would like my business cards to look similar.

Target Market(s)

anyone needing bulldozer and/or tractor services

Industry/Entity Type

Business

Contact Information for Business Card

K & R Acreage Works, Operated by 7-M-Ranch
Doug Pelham
601-473-5826
dpr4178@mailvexo.com

Font styles to use
Sans Serif

Colors

Designer to choose colors to be used in the design.

Requirements
Must have
• image of tractor and bulldozer
• Land Clearing
• Wildlife food plots
• Bush Hogging
• Disking
• Site prep
Nice to have
• i have included a image of a business card that i like. I would like mine to be similar.

```html
<!DOCTYPE html>
<html lang="en">
<head>
<meta charset="utf-8">
<title>K &amp; R Acreage Works – Business Card</title>
<link href="https://fonts.googleapis.com/css2?family=Oswald:wght@500;700&family=Michroma&family=Saira:wght@400;500&display=swap" rel="stylesheet">
<style>
  :root{
    --stage:#1c1c1e;
    --card:#2b2b2d;
    --olive:#8a8431;
    --gold:#b7a24a;
    --silver-light:#e9e9ea;
    --silver-dark:#8d8e91;
    --white:#ffffff;
    --brown:#6b4522;
    --photo-green:#4f6a2e;
    --photo-dark:#2f4220;
    --photo-earth:#9a7a3c;
    --text-light:#f2f2f2;
  }
  *{margin:0;padding:0;box-sizing:border-box}
  html,body{width:1200px;height:900px;overflow:hidden;background:var(--stage)}
  .card{
    position:absolute;left:100px;top:164px;width:1000px;height:572px;
    background:var(--card);overflow:hidden;border-radius:4px;
    box-shadow:0 18px 40px rgba(0,0,0,.55);
  }
  .card-art{position:absolute;inset:0;width:1000px;height:572px}
  .brand-title{
    position:absolute;left:330px;top:22px;
    font-family:"Oswald",sans-serif;font-weight:700;font-size:54px;
    letter-spacing:1px;text-transform:uppercase;color:var(--gold);
    line-height:1;
  }
  .brand-sub{
    position:absolute;left:345px;top:86px;
    font-family:"Oswald",sans-serif;font-weight:500;font-size:22px;
    letter-spacing:1px;text-transform:uppercase;color:var(--white);
  }
  .brand-mark{
    position:absolute;left:430px;top:250px;width:140px;height:140px;
    border-radius:50%;background:var(--silver-light);
    display:flex;align-items:center;justify-content:center;
    font-family:"Oswald",sans-serif;font-weight:700;font-size:44px;color:var(--card);
  }
  .contact{position:absolute;left:70px;top:335px;color:var(--text-light)}
  .contact-name{
    font-family:"Michroma",sans-serif;font-size:30px;text-transform:uppercase;
    letter-spacing:1px;margin-bottom:14px;font-weight:400;
  }
  .contact-line{
    display:flex;align-items:center;gap:12px;
    font-family:"Saira",sans-serif;font-size:26px;margin-bottom:6px;
  }
  .contact-icon{width:24px;height:24px;flex:none}
  .services{
    position:absolute;right:90px;top:394px;list-style:none;text-align:right;
    font-family:"Oswald",sans-serif;font-weight:700;font-size:28px;
    text-transform:uppercase;color:var(--white);line-height:1.12;
  }
  .services li{display:flex;align-items:center;justify-content:flex-end;gap:16px}
  .services li::after{
    content:"";width:13px;height:13px;border-radius:50%;background:var(--silver-light);flex:none;
  }
</style>
</head>
<body>
  <article class="card">
    <svg class="card-art" viewBox="0 0 1000 572">
      <defs>
        <linearGradient id="photoTone" x1="0" y1="0" x2="1" y2="1">
          <stop offset="0" stop-color="var(--photo-dark)"/>
          <stop offset=".45" stop-color="var(--photo-green)"/>
          <stop offset=".75" stop-color="var(--photo-earth)"/>
          <stop offset="1" stop-color="var(--photo-green)"/>
        </linearGradient>
        <linearGradient id="silverTone" x1="0" y1="0" x2="1" y2="0">
          <stop offset="0" stop-color="var(--silver-dark)"/>
          <stop offset=".5" stop-color="var(--silver-light)"/>
          <stop offset="1" stop-color="var(--silver-dark)"/>
        </linearGradient>
      </defs>
      <path role="img" aria-label="Photo of a red tractor and a yellow bulldozer clearing brush in a wooded lot"
            d="M0,0H1000V320C820,312 640,305 500,305C340,305 160,262 0,238Z" fill="url(#photoTone)"/>
      <path class="band-olive" d="M0,238C160,262 340,305 500,305L500,318C330,318 150,285 0,268Z" fill="var(--olive)"/>
      <path class="band-silver" d="M0,268C150,285 330,318 500,318L500,335C320,335 140,308 0,296Z" fill="url(#silverTone)"/>
      <path class="band-silver" d="M500,305C640,305 820,312 1000,320V340C820,332 640,325 500,325Z" fill="url(#silverTone)"/>
      <path class="band-white" d="M500,325C640,325 820,332 1000,340V354C820,346 640,339 500,339Z" fill="var(--white)"/>
      <path class="band-brown" d="M500,339C640,339 820,346 1000,354V378C820,368 650,358 500,355Z" fill="var(--brown)"/>
    </svg>

    <h1 class="brand-title">K &amp; R Acreage Works</h1>
    <p class="brand-sub">Operated by 7-M-Ranch</p>

    <div class="brand-mark">K&amp;R</div>

    <section class="contact">
      <h2 class="contact-name">Doug Pelham</h2>
      <p class="contact-line">
        <svg class="contact-icon" viewBox="0 0 24 24"><circle cx="12" cy="12" r="12" fill="var(--gold)"/><path d="M8 6l2.5 0 1 3-1.5 1.2a8 8 0 0 0 3.8 3.8L15 12.5l3 1v2.5c0 .8-.7 1.2-1.5 1.1A11 11 0 0 1 6.9 7.5C6.8 6.7 7.2 6 8 6z" fill="var(--card)"/></svg>
        601-473-5826
      </p>
      <p class="contact-line">
        <svg class="contact-icon" viewBox="0 0 24 24"><circle cx="12" cy="12" r="12" fill="var(--gold)"/><rect x="6" y="8" width="12" height="8" rx="1" fill="var(--card)"/><path d="M6.5 8.5L12 12.5l5.5-4" stroke="var(--gold)" stroke-width="1.3" fill="none"/></svg>
        dpr4178@mailvexo.com
      </p>
    </section>

    <ul class="services">
      <li>Land Clearing</li>
      <li>Wildlife Food Plots</li>
      <li>Bush Hogging</li>
      <li>Disking</li>
      <li>Site Prep</li>
    </ul>
  </article>
</body>
</html>
```